Fun, Clean Business Card For Family Focused Travel Agency

I need a business card using specific colors and fonts as in the uploaded files. Ideally, I would like a large image of the logo on the back and all the contact info on the front. Maybe the stars/dots somewhere in a flowy form.

I do want it the contact information to be clear and easy to read. I don't want it to look too busy. Maybe even a bit minimalist.

I plan or ordering the ROUNDED CORNER business cards from Cardwell Press, so please consider that in your design.

Target Market(s)

Families with children, couples, groups of friends

Contact Information for Business Card

Marla Quent, Owner
Marla@TidewayTrips.example
Cell Phone Number 555-218-6034
Office Phone Number 555-647-1295
Specializing in Fablecrest destinations, Goldmere Parkside Resort, Cruises and All-Inclusive Vacations.

Nice but not required:
www.TidewayTrips.example
Facebook, Instagram, Twitter icons with username: TidewayTrips

Font styles to use
Sans Serif

Requirements
Must have
• Please try to use the colors from the logo as much as possible. I understand lighter shades/colors may be needed for some things.
Should not have
• NO SERIF FONTS. That is really the only thing I do not want at all

```html
<!DOCTYPE html>
<html lang="en">
<head>
<meta charset="utf-8">
<title>Tideway Trips – Business Card</title>
<link rel="stylesheet" href="https://fonts.googleapis.com/css2?family=Overpass:wght@400;600;700&family=Yellowtail&display=swap">
<style>
  :root {
    --bg: #2a2a2c;
    --card: #f7f7f6;
    --navy: #1d2037;
    --teal: #1aa58a;
    --sky: #4a8fd6;
    --orange: #e98a2c;
  }
  * { box-sizing: border-box; margin: 0; padding: 0; }
  html, body { width: 1200px; height: 900px; overflow: hidden; }
  body {
    background: var(--bg);
    font-family: "Overpass", sans-serif;
    color: var(--navy);
    position: relative;
  }
  .card {
    position: absolute;
    left: 230px;
    width: 740px;
    height: 423px;
    background: var(--card);
    border-radius: 34px;
    box-shadow: 0 10px 30px rgba(0,0,0,.45);
  }
  .card--front { top: 20px; }
  .card--back { top: 457px; }

  /* front */
  .brand {
    position: absolute;
    left: 0; right: 0; top: 150px;
    display: flex; align-items: center; justify-content: center; gap: 22px;
  }
  .brand__dot {
    width: 96px; height: 96px; border-radius: 50%;
    background: var(--teal);
  }
  .brand__name {
    font-weight: 700; font-size: 70px; line-height: 1;
    color: var(--navy); letter-spacing: -1px;
  }

  /* back */
  .person { position: absolute; left: 80px; top: 150px; width: 280px; text-align: center; }
  .person__name {
    font-family: "Yellowtail", "Overpass", sans-serif;
    font-size: 46px; line-height: 1.1; color: var(--navy);
    white-space: nowrap;
  }
  .person__role { font-size: 20px; letter-spacing: 1px; color: var(--teal); margin-top: 2px; }

  .contact { position: absolute; left: 390px; top: 138px; list-style: none; }
  .contact__item { display: flex; align-items: center; gap: 12px; font-size: 18px; height: 32px; white-space: nowrap; }
  .contact__item svg { width: 18px; height: 18px; fill: var(--teal); flex: none; }
  .contact__social { margin-top: 8px; }
  .contact__social .square { width: 16px; height: 16px; background: var(--teal); border-radius: 3px; flex: none; }
  .contact__web { color: var(--teal); font-size: 19px; height: 28px; display: block; white-space: nowrap; }

  .services {
    position: absolute; left: 34px; right: 30px; bottom: 46px;
    display: flex; justify-content: space-between; list-style: none;
    font-size: 15.5px; color: var(--navy);
  }
  .services li { display: flex; align-items: center; gap: 5px; white-space: nowrap; }
  .services svg { width: 13px; height: 13px; flex: none; }
</style>
</head>
<body>
  <section class="card card--front">
    <div class="brand">
      <span class="brand__dot"></span>
      <span class="brand__name">Tideway Trips</span>
    </div>
  </section>

  <section class="card card--back">
    <div class="person">
      <div class="person__name">Marla Quent</div>
      <div class="person__role">OWNER</div>
    </div>

    <ul class="contact">
      <li class="contact__item">
        <svg viewBox="0 0 24 24"><path d="M7 1h10a2 2 0 0 1 2 2v18a2 2 0 0 1-2 2H7a2 2 0 0 1-2-2V3a2 2 0 0 1 2-2zm0 3v14h10V4zm5 15.5a1.2 1.2 0 1 0 0 2.4 1.2 1.2 0 0 0 0-2.4z"/></svg>
        555-218-6034
      </li>
      <li class="contact__item">
        <svg viewBox="0 0 24 24"><path d="M2 8c0-3 5-4 10-4s10 1 10 4v2h-5V8H7v2H2zm3 4h14l2 8H3zm7 1.5a2.5 2.5 0 1 0 0 5 2.5 2.5 0 0 0 0-5z"/></svg>
        555-647-1295
      </li>
      <li class="contact__item">
        <svg viewBox="0 0 24 24"><path d="M2 5h20v14H2zm2 2v.4l8 5.4 8-5.4V7zm0 2.8V17h16V9.8l-8 5.4z"/></svg>
        Marla@TidewayTrips.example
      </li>
      <li class="contact__item contact__social">
        <span class="square"></span>
        TidewayTrips
      </li>
      <li><span class="contact__web">www.TidewayTrips.example</span></li>
    </ul>

    <ul class="services">
      <li><svg viewBox="0 0 20 20"><path fill="#1d2037" d="M10 0l2.2 7.8L20 10l-7.8 2.2L10 20l-2.2-7.8L0 10l7.8-2.2z"/></svg>Fablecrest destinations</li>
      <li><svg viewBox="0 0 20 20"><path fill="#1aa58a" d="M10 0l2.2 7.8L20 10l-7.8 2.2L10 20l-2.2-7.8L0 10l7.8-2.2z"/></svg>Goldmere Parkside Resort</li>
      <li><svg viewBox="0 0 20 20"><path fill="#4a8fd6" d="M10 0l2.2 7.8L20 10l-7.8 2.2L10 20l-2.2-7.8L0 10l7.8-2.2z"/></svg>Cruises and All-Inclusive Vacations</li>
    </ul>
  </section>
</body>
</html>
```